Paws Home

Need Yard signs
Dimensions 24" wide and 18" high

Copy: Rescue does not mean "Damaged". It means they have been let down by humans.
Please adopt at: 217 W Brannock Ave, Tampa, Fl 33682
Open: Tues-Sun 10am - 7pm

I have attached a sample of the original ad. I can't use this because the resolution is too low and the type has to be big enough so that it can be seen 12 feet away.
I have also attached some photos you can use. The res may not be hi enough, but perhaps you can find some stock photography even these pics are not hi res enough.

Target Market(s)

animal lovers

Font styles to use
Sans Serif

Colors

Designer to choose colors to be used in the design.

Requirements
Must have
• Must be easy to read.

```html
<!DOCTYPE html>
<html lang="en">
<head>
<meta charset="utf-8">
<title>Paws Home – Yard Sign</title>
<link rel="stylesheet" href="https://fonts.googleapis.com/css2?family=Rubik+Distressed&family=Arimo:wght@700&display=swap">
<style>
  :root {
    --page: #e9e9ea;
    --sign-black: #0a0a0a;
    --amber: #f5a83a;
    --alert-red: #e1262c;
    --white: #ffffff;
    --brand-blue: #2b9ed6;
    --photo-warm: #7a4a26;
    --photo-dark: #1a120c;
  }
  * { margin: 0; padding: 0; box-sizing: border-box; }
  html, body {
    width: 939px; height: 1200px; overflow: hidden;
    background: var(--page);
  }
  .yard-sign {
    position: absolute;
    left: 20px; top: 262px;
    width: 900px; height: 675px;
    background: var(--sign-black);
    overflow: hidden;
    box-shadow: 0 2px 8px rgba(0,0,0,.25);
  }
  .hero-photo {
    position: absolute;
    left: 330px; top: 0; width: 570px; height: 675px;
    background:
      radial-gradient(ellipse 55% 45% at 45% 40%, #5b4a3e 0%, transparent 70%),
      radial-gradient(ellipse 40% 55% at 80% 55%, var(--photo-warm) 0%, transparent 75%),
      radial-gradient(ellipse 70% 70% at 55% 50%, #3a2618 0%, var(--photo-dark) 70%, var(--sign-black) 100%);
  }
  .hero-photo::before {
    content: ""; position: absolute; inset: 0;
    background: linear-gradient(90deg, var(--sign-black) 0%, transparent 30%);
  }
  .brand-name {
    position: absolute; right: 30px; top: 24px;
    font-family: "Arimo", sans-serif; font-weight: 700;
    font-size: 28px; color: var(--brand-blue); letter-spacing: .5px;
  }
  .headline {
    position: absolute; left: 0; top: 0;
    font-family: "Rubik Distressed", sans-serif;
    text-transform: uppercase;
  }
  .headline span {
    position: absolute; white-space: nowrap;
    transform-origin: left top;
    transform: scaleX(.62);
    line-height: 1;
  }
  .line-rescue   { left: 60px;  top: 40px;  font-size: 92px; color: var(--amber); }
  .line-notmean  { left: 113px; top: 122px; font-size: 52px; color: var(--white); }
  .line-damaged  { left: 42px;  top: 160px; font-size: 100px; color: var(--alert-red); }
  .line-means    { left: 112px; top: 242px; font-size: 54px; color: var(--white); }
  .line-letdown  { left: 65px;  top: 290px; font-size: 54px; color: var(--white); }
  .line-downby   { left: 125px; top: 338px; font-size: 54px; color: var(--white); }
  .line-humans   { left: 62px;  top: 372px; font-size: 96px; color: var(--amber); }
  .opening-hours {
    position: absolute; left: 45px; top: 494px;
    font-family: "Rubik Distressed", sans-serif;
    font-size: 40px; color: var(--sign-black);
    -webkit-text-stroke: 1.5px var(--white);
    text-shadow: 0 0 2px var(--white);
    white-space: nowrap; line-height: 1;
    transform-origin: left top; transform: scaleX(.62);
  }
  .adopt-label {
    position: absolute; left: 42px; top: 556px;
    font-family: "Arimo", sans-serif; font-weight: 700;
    font-size: 22px; color: var(--amber);
  }
  .adopt-address {
    position: absolute; left: 42px; top: 584px;
    font-family: "Arimo", sans-serif; font-weight: 700;
    font-size: 27px; line-height: 31px; color: var(--white);
  }
</style>
</head>
<body>
  <main class="yard-sign">
    <div class="hero-photo" role="img" aria-label="Close-up of a rescue dog's nose pressed against a chain-link fence"></div>
    <div class="brand-name">Paws Home</div>
    <h1 class="headline">
      <span class="line-rescue">Rescue</span>
      <span class="line-notmean">does not mean</span>
      <span class="line-damaged">Damaged</span>
      <span class="line-means">it means they</span>
      <span class="line-letdown">have been let</span>
      <span class="line-downby">down by</span>
      <span class="line-humans">Humans</span>
    </h1>
    <p class="opening-hours">OPEN TUES-SUN 10AM-7PM</p>
    <p class="adopt-label">Please adopt at:</p>
    <p class="adopt-address">217 W Brannock Ave,<br>Tampa, Fl 33682</p>
  </main>
</body>
</html>
```